German CBD company needs a label+packaging design (templates provided)

Hey there,
we are a German e-commerce company and about to launch a CBD E-liquid series under our new brand "VELMORIQ". We need designs for the cardbord tube packaging and the labels of bottles. Find attached templates for both, the labels and the packaging. The templates already have a design on them just for you to know that some space will be filled with legal information. Feel free to use the templates and change the designs and of course we have the suitable text down below. Every outer packaging label and bottle label should include the brand name "VELMORIQ" (we typically use the font Archivo Black, but feel free to change it, if you have a better idea), the CBD content, the flavour and the filling quantity (10ml). You can use 100mg and Mango for your design and if your design wins, we will work with you and change the flavours and concentrations for the other liquids accordingly. Our liquids are Made in Germany and of a very high quality so we are looking for a premium design that underlines the quality und purity of our product. Something between luxurious and futuristic. Please let your creativity run wild :)

As for the packaging we need the following texts on the packaging:

DE:
(bold)Inhaltsstoffe:(bold) < 70% Propylen Glycol, < 30% VG Glycerol, Aromen, Cannabidiol (CBD) wie angegeben CAS 13956-29-1.
(bold)Anwendung(bold) Vor Benutzung schütteln. Dieses Produkt ist unverdünnt in einer kompatiblen e-Zigarette anzuwenden. 2-3 Züge inhalieren. Zwischen den Anwendungen 10-20 Minuten warten. Dieses Produkt ersetzt keine ausgewogene Ernährung.
(bold)Hinweise:(bold) VELMORIQ CBD e-Liquids sind Tabakersatzprodukte gem. TPD2 und bestehen aus organischen und zertifizierten, >99% reinen CBD-Kristallen. HACCP & GMP konform. Nicht empfohlen für Schwangere, stillende Frauen oder Nichtraucher. Dieses Produkt ist nicht zur Diagnose, Behandlung, Heilung oder Vorbeugung von Krankheiten bestimmt. Darf nicht in die Hände von Kindern und Jugendlichen gelangen. Keine Abgabe unter 18 Jahren. Dunkel und kühl lagern. Nicht zum Verzehr geeignet.

EN:
(bold)Ingredients:(bold) < 70% Propylen Glycol, < 30% VG Glycerol, flavours , Cannabidiol (CBD).
(bold)Application(bold): Shake before use. This product should be applied undiluted in a compatible e-cigarette. Inhale 2-3 puffs. Wait 10-20 minutes until using again.
(bold)Notes(bold): VELMORIQ e-liquids are made from organic and certified >99% pure CBD Crystals. HACCP & GMP compliant. Not recommended for pregnant or breastfeeding women or non-smokers.
This product is not intended to diagnose, treat, cure or prevent any disease. Keep away from children. No sale to minors. Store in a cool, dark place. Not for consumption.

DE: Qualität:
Wir verwenden für unsere Liquids organische und zertifizierte CBD-Kristalle von >99% Reinheit. Wir verwenden nur die hochwertigsten Rohstoffe zur Herstellung unserer Liquids, um unseren Kunden ein optimales Vape-Erlebnis bieten zu können.
EN: Quality:
We use organic and certified CBD-Crystals with a purity >99%. We only use the highest quality raw material for the production of our liquids in order to ensure an optimal vaping experience for our customers.

Please consider that we will also need space for our contact information, our website URL and an EAN bar code.

Now the label for the bottles: As already said our templates have designs on them, so please feel free to change anything you like. It`s just an example of the label printing company so we could get an idea. We just need the following texts on those labels:
DE:(bold)Inhaltsstoffe:(bold) < 70% Propylen Glycol, < 30% VG Glycerol, Aromen, Cannabidiol (CBD) wie angegeben CAS 13956-29-1.
Darf nicht in die Hände von Kindern und Jugendlichen gelangen. Keine Abgabe unter 18 Jahren.

EN:(bold)Ingredients:(bold) < 70% Propylen Glycol, < 30% VG Glycerol, flavours , Cannabidiol (CBD).
Keep away from children. No sale to minors.
Moreover, we need the symbols that are already on the label and some space for an EAN bar code. The labels should include CBD content, brand name, flavour..(see above)

I hope our briefing is clear enough. If you have any further questions, please contact me via e-mail (olek.dravin@quenlo-shop.example).
We are looking forwards to receiving your designs and doing some further work with you. We know that it`s more than one simple task, so we are willing to pay a little bonus for the further work which we will do with the winner :)

Greetings from Frankfurt, Germany
Quenlo GmbH Team
Olek Dravin
olek.dravin@quenlo-shop.example

Font styles to use
Other font styles liked:
• Archivo Black (not mandatory, just an idea)

Colors

Designer to choose colors to be used in the design.

Requirements
Must have
• - Legal notices as mentioned above
• - CBD content in mg
• - flavour
• - space for EAN bar code & contact information
Should not have
• - shouldn`t look too clean, not like a medicine

```html
<!DOCTYPE html>
<html lang="en">
<head>
<meta charset="utf-8">
<title>VELMORIQ – Label</title>
<link rel="stylesheet" href="https://fonts.googleapis.com/css2?family=Oranienbaum&family=Jost:wght@300;400&display=swap">
<style>
  :root {
    --ink-dark: #171c16;
    --paper: #f3f3f2;
    --paper-shade: #e4e5e3;
    --green-deep: #243a2a;
    --green-mid: #3f5d47;
    --white: #ffffff;
    --fine-grey: #6f746f;
  }
  * { margin: 0; padding: 0; box-sizing: border-box; }
  html, body {
    width: 1200px; height: 914px; overflow: hidden;
    background: var(--ink-dark);
  }
  .canvas {
    position: relative; width: 1200px; height: 914px;
    background: var(--ink-dark); overflow: hidden;
  }

  /* Left: brand lockup */
  .brand-lockup {
    position: absolute; left: 117px; top: 296px;
    font-family: "Oranienbaum", serif; font-weight: 400;
    color: var(--white);
    font-size: 92px; line-height: 76px;
    letter-spacing: -1px;
    transform: scaleX(0.84); transform-origin: left top;
  }
  .company {
    position: absolute; left: 117px; top: 612px;
    display: flex; gap: 14px; align-items: flex-start;
  }
  .company-mark {
    width: 42px; height: 42px; border-radius: 50%;
    background: var(--white); margin-top: 14px;
  }
  .company-details {
    font-family: "Jost", sans-serif; font-weight: 400;
    font-size: 8.4px; line-height: 14.8px; letter-spacing: 0.2px;
    color: var(--white); list-style: none;
  }

  /* Right: label */
  .label {
    position: absolute; left: 585px; top: 0; width: 540px; height: 914px;
    background: linear-gradient(90deg, var(--paper-shade) 0%, var(--paper) 18%, #fafafa 55%, var(--paper) 85%, var(--paper-shade) 100%);
    overflow: hidden;
  }
  .label-name {
    position: absolute; left: -30px; top: 22px;
    padding-bottom: 90px;
    font-family: "Oranienbaum", serif; font-weight: 400;
    font-size: 320px; line-height: 236px;
    letter-spacing: -4px;
    background: linear-gradient(180deg, var(--green-mid) 0%, var(--green-deep) 55%, var(--green-mid) 100%);
    -webkit-background-clip: text; background-clip: text;
    color: transparent;
    transform: scaleX(0.66); transform-origin: left top;
    white-space: nowrap;
  }
  .flavour {
    position: absolute; left: 52px; top: 583px;
    font-family: "Jost", sans-serif; font-weight: 300;
    font-size: 17px; letter-spacing: 3px;
    color: #3a3d3a;
    transform: rotate(1.8deg); transform-origin: left center;
  }
  .strength {
    position: absolute; left: 1088px;
    font-family: "Jost", sans-serif; font-weight: 300;
    font-size: 12px; line-height: 14px; letter-spacing: 3px; color: var(--fine-grey);
    transform: rotate(-90deg); transform-origin: left top;
    white-space: nowrap;
  }
  .strength-percent { top: 424px; }
  .strength-dose { top: 290px; }
  .leaf-artwork {
    position: absolute; left: 69px; top: 676px; width: 218px; height: 212px;
    background: radial-gradient(ellipse at 50% 60%, var(--green-mid) 0%, var(--green-deep) 40%, rgba(36,58,42,0.25) 62%, rgba(36,58,42,0) 72%);
  }
</style>
</head>
<body>
<main class="canvas">
  <section class="brand-side">
    <h1 class="brand-lockup">VELM<br>ORIQ</h1>
    <div class="company">
      <span class="company-mark"></span>
      <ul class="company-details">
        <li>KORVUCARE GMBH, GERMANY</li>
        <li>KORVU LABORATORIES</li>
        <li>LINDENWEG 12</li>
        <li>D-25711 HALSTEDT</li>
        <li>WWW.KORVU-CARE.EXAMPLE</li>
      </ul>
    </div>
  </section>

  <section class="label">
    <div class="label-name">VELM<br>ORIQ</div>
    <p class="flavour">MANGO FLAVOUR</p>
    <div class="leaf-artwork" role="img" aria-label="Green leaf illustration"></div>
  </section>
  <p class="strength strength-percent">1%</p>
  <p class="strength strength-dose">100mg/10ml CBD</p>
</main>
</body>
</html>
```